Aviation security consulting company needs a website

We need a website design for Brisk Holloway, and aviation security consulting company. Brisk Holloway (www.briskholloway.example) is an aviation security consulting company that works with government and industry stakeholders in over 60 countries on aviation security strategy, governance, and oversight at the regulatory and operational level.
Brisk Holloway is strongly internationally focused.
The website required should be simple, corporate, serious, and communicate professionalism, reliability and honesty. We are trying to give the company a feeling of being well established.
The attached files include the company logo, along with examples of company web page styles that we like.
The Brisk Holloway website need only be around five pages long (landing page, who we are, our services, our clients, contact), though don't feel limited to only five pages.
The existing website (www.briskholloway.example) was rushed and put together using Wix. We don't love the existing website as it looks too amateur, so don't use it as a template.
There is no requirement for any online sales tools to be included in the site. The site is purely informational, with the option of people making contact via email.

```html
<!DOCTYPE html>
<html lang="en">
<head>
<meta charset="utf-8">
<title>About — Brisk Holloway</title>
<link href="https://fonts.googleapis.com/css2?family=Arimo:wght@400;700&display=swap" rel="stylesheet">
<style>
  :root {
    --navy: #0c1a3e;
    --ink: #1d1d1d;
    --muted: #777777;
    --link: #2a6ebb;
    --rule: #e4e4e4;
    --panel: #f5f5f5;
    --placeholder: #cccccc;
    --card-border: #dddddd;
    --social: #2f6db3;
    --nav-text: #9aa3b5;
    --nav-active: #eeeeee;
  }
  * { box-sizing: border-box; margin: 0; padding: 0; }
  html, body { width: 667px; height: 1200px; overflow: hidden; background: #ffffff; }
  body { font-family: "Arimo", Arial, sans-serif; color: var(--ink); position: relative; }

  .site-nav { position: absolute; left: 0; top: 0; width: 667px; height: 53px; background: var(--navy); }
  .brand { position: absolute; left: 20px; top: 12px; display: flex; align-items: center; gap: 8px; }
  .brand-mark { width: 26px; height: 26px; background: #ffffff; }
  .brand-name { color: #ffffff; font-size: 20px; font-weight: 700; letter-spacing: -0.3px; white-space: nowrap; }
  .nav-links { position: absolute; left: 333px; top: 0; display: flex; list-style: none; height: 33px; white-space: nowrap; }
  .nav-links li { font-size: 10.5px; font-weight: 700; color: var(--nav-text); padding: 0 8px; line-height: 33px; white-space: nowrap; }
  .nav-links li.active { background: var(--nav-active); color: #555; padding: 0 9px; }
  .caret { display: inline-block; border-left: 3px solid transparent; border-right: 3px solid transparent; border-top: 3px solid var(--nav-text); margin-left: 4px; vertical-align: middle; }

  .page-title { position: absolute; left: 20px; top: 60px; width: 627px; padding-bottom: 8px; border-bottom: 1px solid var(--rule); }
  .page-title h1 { font-size: 26px; font-weight: 700; }
  .page-title small { font-size: 17px; color: var(--muted); margin-left: 4px; }

  .breadcrumb { position: absolute; left: 20px; top: 106px; width: 627px; height: 24px; background: var(--panel); border-radius: 3px; font-size: 10px; font-weight: 700; line-height: 24px; padding-left: 10px; }
  .breadcrumb a { color: var(--link); text-decoration: none; }
  .breadcrumb .sep { color: #bbb; margin: 0 6px; }
  .breadcrumb .current { color: #555; }

  .about-photo { position: absolute; left: 20px; top: 143px; width: 303px; height: 182px; background: var(--placeholder); }
  .about-copy { position: absolute; left: 344px; top: 156px; width: 303px; }
  .about-copy h2 { font-size: 21px; font-weight: 700; margin-bottom: 8px; }
  .about-copy p { font-size: 9.6px; font-weight: 700; line-height: 1.4; margin-bottom: 8px; }

  .section-title { position: absolute; left: 20px; width: 627px; font-size: 20px; font-weight: 700; padding-bottom: 8px; border-bottom: 1px solid var(--rule); }

  .team-grid { position: absolute; left: 20px; top: 434px; width: 627px; display: grid; grid-template-columns: repeat(3, 195px); column-gap: 21px; row-gap: 14px; }
  .member-card { height: 258px; border: 1px solid var(--card-border); border-radius: 4px; padding: 3px; text-align: center; }
  .member-photo { height: 113px; background: var(--placeholder); }
  .member-name { font-size: 16px; font-weight: 700; margin-top: 19px; }
  .member-role { font-size: 11px; font-weight: 700; color: var(--muted); margin-top: 4px; }
  .member-bio { font-size: 9.6px; font-weight: 700; line-height: 1.35; margin: 8px 4px 0; }
  .social-row { display: flex; justify-content: center; gap: 9px; margin-top: 6px; }
  .social-row span { width: 15px; height: 15px; background: var(--social); border-radius: 3px; }

  .customer-row { position: absolute; left: 20px; top: 1047px; width: 627px; display: flex; justify-content: space-between; }
  .customer-logo { width: 88px; height: 53px; background: var(--placeholder); }

  .site-footer { position: absolute; left: 20px; top: 1111px; width: 627px; border-top: 1px solid var(--rule); padding-top: 36px; font-size: 10px; font-weight: 700; }
</style>
</head>
<body>
  <nav class="site-nav">
    <div class="brand"><span class="brand-mark"></span><span class="brand-name">Brisk Holloway</span></div>
    <ul class="nav-links">
      <li class="active">About</li>
      <li>Services</li>
      <li>Contact</li>
      <li>Portfolio<span class="caret"></span></li>
      <li>Other Pages<span class="caret"></span></li>
    </ul>
  </nav>

  <header class="page-title"><h1>About <small>Subheading</small></h1></header>
  <div class="breadcrumb"><a href="#">Home</a><span class="sep">/</span><span class="current">About</span></div>

  <div class="about-photo" role="img" aria-label="Photo of the Brisk Holloway team at work"></div>
  <section class="about-copy">
    <h2>About Brisk Holloway</h2>
    <p>Lorem ipsum dolor sit amet, consectetur adipisicing elit. Sed voluptate nihil eum consectetur similique? Consectetur, quod, incidunt, harum nisi dolores delectus reprehenderit voluptatem perferendis dicta dolorem non blanditiis ex fugiat.</p>
    <p>Lorem ipsum dolor sit amet, consectetur adipisicing elit. Saepe, magni, aperiam vitae illum voluptatum aut sequi impedit non velit ab ea pariatur sint quidem corporis eveniet. Odit, temporibus reprehenderit dolorum!</p>
    <p>Lorem ipsum dolor sit amet, consectetur adipisicing elit. Et, consequuntur, modi mollitia corporis ipsa voluptate corrupti eum ratione ex ea praesentium quibusdam? Aut, in eum facere corrupti necessitatibus perspiciatis quis?</p>
  </section>

  <h2 class="section-title" style="top:390px">Our Team</h2>
  <div class="team-grid">
    <article class="member-card"><div class="member-photo" role="img" aria-label="Team member portrait"></div><h3 class="member-name">John Doe</h3><div class="member-role">Job Title</div><p class="member-bio">Lorem ipsum dolor sit amet, consectetur adipisicing elit. Iste saepe et quisquam nesciunt maxime.</p><div class="social-row"><span aria-label="Social profile"></span><span aria-label="Social profile"></span><span aria-label="Social profile"></span></div></article>
    <article class="member-card"><div class="member-photo" role="img" aria-label="Team member portrait"></div><h3 class="member-name">John Doe</h3><div class="member-role">Job Title</div><p class="member-bio">Lorem ipsum dolor sit amet, consectetur adipisicing elit. Iste saepe et quisquam nesciunt maxime.</p><div class="social-row"><span aria-label="Social profile"></span><span aria-label="Social profile"></span><span aria-label="Social profile"></span></div></article>
    <article class="member-card"><div class="member-photo" role="img" aria-label="Team member portrait"></div><h3 class="member-name">John Doe</h3><div class="member-role">Job Title</div><p class="member-bio">Lorem ipsum dolor sit amet, consectetur adipisicing elit. Iste saepe et quisquam nesciunt maxime.</p><div class="social-row"><span aria-label="Social profile"></span><span aria-label="Social profile"></span><span aria-label="Social profile"></span></div></article>
    <article class="member-card"><div class="member-photo" role="img" aria-label="Team member portrait"></div><h3 class="member-name">John Doe</h3><div class="member-role">Job Title</div><p class="member-bio">Lorem ipsum dolor sit amet, consectetur adipisicing elit. Iste saepe et quisquam nesciunt maxime.</p><div class="social-row"><span aria-label="Social profile"></span><span aria-label="Social profile"></span><span aria-label="Social profile"></span></div></article>
    <article class="member-card"><div class="member-photo" role="img" aria-label="Team member portrait"></div><h3 class="member-name">John Doe</h3><div class="member-role">Job Title</div><p class="member-bio">Lorem ipsum dolor sit amet, consectetur adipisicing elit. Iste saepe et quisquam nesciunt maxime.</p><div class="social-row"><span aria-label="Social profile"></span><span aria-label="Social profile"></span><span aria-label="Social profile"></span></div></article>
    <article class="member-card"><div class="member-photo" role="img" aria-label="Team member portrait"></div><h3 class="member-name">John Doe</h3><div class="member-role">Job Title</div><p class="member-bio">Lorem ipsum dolor sit amet, consectetur adipisicing elit. Iste saepe et quisquam nesciunt maxime.</p><div class="social-row"><span aria-label="Social profile"></span><span aria-label="Social profile"></span><span aria-label="Social profile"></span></div></article>
  </div>

  <h2 class="section-title" style="top:1004px">Our Customers</h2>
  <div class="customer-row">
    <div class="customer-logo" role="img" aria-label="Customer logo"></div>
    <div class="customer-logo" role="img" aria-label="Customer logo"></div>
    <div class="customer-logo" role="img" aria-label="Customer logo"></div>
    <div class="customer-logo" role="img" aria-label="Customer logo"></div>
    <div class="customer-logo" role="img" aria-label="Customer logo"></div>
    <div class="customer-logo" role="img" aria-label="Customer logo"></div>
  </div>

  <footer class="site-footer">Copyright © Your Website 2014</footer>
</body>
</html>
```